THE TALL COPPER ATLAS OF PORTS

subtitle: AN INTRO TO SEARCH ENGINE OPTIMIZATION
background: white
dimensions: 1562x2500

Target Market(s)

Marketing professionals

Industry/Entity Type

Digital Marketing

Font styles to use
Sans Serif

Colors
ffffff
1b1b1b
3176b5

Requirements
Should not have
• Images or graphics

```html
<!DOCTYPE html>
<html lang="en">
<head>
<meta charset="utf-8">
<title>The Tall Copper Atlas of Ports – Book Cover</title>
<link rel="stylesheet" href="https://fonts.googleapis.com/css2?family=Bebas+Neue&family=Barlow:wght@700&display=swap">
<style>
  :root {
    --paper: #ffffff;
    --ink: #1b1b1b;
    --blue: #3176b5;
    --backdrop: #808080;
    --depth: rgba(27, 27, 27, 0.85);
  }
  html, body {
    margin: 0;
    width: 1200px;
    height: 1200px;
    overflow: hidden;
    background: var(--backdrop);
  }
  .cover {
    position: absolute;
    left: 255px;
    top: 48px;
    width: 690px;
    height: 1104px;
    background: var(--paper);
    overflow: hidden;
  }
  .author {
    position: absolute;
    left: 0;
    right: 0;
    top: 56px;
    margin: 0;
    text-align: center;
    font-family: "Barlow", Arial, sans-serif;
    font-weight: 700;
    font-size: 46px;
    line-height: 1;
    letter-spacing: 0.33em;
    padding-left: 0.33em;
    color: var(--ink);
  }
  .book-title {
    position: absolute;
    left: 0;
    right: 0;
    top: 140px;
    margin: 0;
    text-align: center;
    font-family: "Barlow", Arial, sans-serif;
    font-weight: 700;
    font-size: 22px;
    line-height: 1;
    letter-spacing: 0.2em;
    padding-left: 0.2em;
    color: var(--ink);
  }
  .title {
    margin: 0;
    font-family: "Bebas Neue", "Oswald", Arial, sans-serif;
    font-weight: 400;
    color: var(--blue);
  }
  .title-line {
    position: absolute;
    left: 40px;
    display: block;
    line-height: 1;
    white-space: nowrap;
    text-shadow: 2px 4px 0 var(--depth);
  }
  .title-line--small { font-size: 112px; }
  .title-line--an { top: 232px; }
  .title-line--intro { top: 356px; }
  .title-line--large { font-size: 190px; }
  .title-line--search { top: 474px; letter-spacing: 0.04em; }
  .title-line--engine { top: 653px; letter-spacing: 0.07em; }
  .title-line--optimization {
    top: 830px;
    font-size: 184px;
    transform: scaleX(0.8);
    transform-origin: left top;
  }
  .initial {
    color: var(--ink);
    text-shadow: 2px 4px 0 #000;
  }
</style>
</head>
<body>
  <main class="cover">
    <p class="author">AUTHOR NAME</p>
    <p class="book-title">THE TALL COPPER ATLAS OF PORTS</p>
    <h1 class="title">
      <span class="title-line title-line--small title-line--an">AN</span>
      <span class="title-line title-line--small title-line--intro">INTRO TO</span>
      <span class="title-line title-line--large title-line--search"><span class="initial">S</span>EARCH</span>
      <span class="title-line title-line--large title-line--engine"><span class="initial">E</span>NGINE</span>
      <span class="title-line title-line--optimization"><span class="initial">O</span>PTIMIZATION</span>
    </h1>
  </main>
</body>
</html>
```